Welbourne Dental, P.C. New stationary and business card for modern Dental Office

We need a new stationary/envelope/business card design using our newly designed logo. We are looking for an upscale look. Our new logo is used on our signage, using black as the background and white for the lettering. We would like the stationary to have black, white, possible greys or silver. We are looking for a letterhead, envelope, and business card design for three different employees, as well as a 4th card, same design, but just general with no employee name.

Project Deadline Extended
Reason: We began this project in the middle of our move into our new office. Things got pretty hectic and we just didn't have the time to go through designs. We now settled in and finally eliminated the designs that didn't work for us. We would like to extend the project another 5 days, and then finalize our decision. Most of the submissions showed business cards alone, with no stationary designs. Our original request was for stationary and business cards. Please keep this in mind.

Target Market(s)

Dental patients expecting high quality, cosmetic dentistry

Industry/Entity Type

Business

Contact Information for Business Card

Will need a design using our logo. All cards will be the same, other than that one card will have Office Managers name, One for the Doctor, Hygienist,
1. Office Manager - Marisol Dubrovka
2. Hygienist - Kayleigh Morrow
3. Gordon T. Welbourne, D.D.S.
4. One general one with no staff names

Font styles to use
Other font styles liked:
• see upload

Colors
000000
1b1b1b
757575
c9c9c9
e8e8e8
ffffff

Requirements
Must have
• -Logo
• -Phone number (718)555-0193
• -Address: 4352 63rd Ave
• Lower Level
• Brooklyn, NY 11290

```html
<!DOCTYPE html>
<html lang="en">
<head>
<meta charset="utf-8">
<title>Welbourne Dental, P.C. — Stationery Set</title>
<link href="https://fonts.googleapis.com/css2?family=Open+Sans:wght@300;400;600;700&display=swap" rel="stylesheet">
<style>
  :root{
    --black:#000000;
    --ink:#1b1b1b;
    --grey-dark:#757575;
    --grey-mid:#9a9a9a;
    --grey-light:#c9c9c9;
    --grey-pale:#e8e8e8;
    --white:#ffffff;
    --backdrop:#d6d6d6;
  }
  *{box-sizing:border-box;margin:0;padding:0}
  html,body{width:1200px;height:800px;overflow:hidden}
  body{background:var(--backdrop);font-family:"Open Sans",Arial,sans-serif;color:var(--ink);position:relative}
  .sheet{position:absolute;background:var(--white);box-shadow:0 2px 10px rgba(0,0,0,.18);overflow:hidden}
  .band{position:absolute;background:var(--grey-light);color:var(--white);font-weight:700;text-transform:uppercase;letter-spacing:.02em;display:flex;align-items:center;white-space:nowrap}
  .band--dark{background:var(--grey-mid)}

  /* brand lockup */
  .brand{position:absolute;display:flex;align-items:center;gap:6px}
  .brand__mark{border:1.5px solid var(--grey-dark);border-radius:50%;flex:none}
  .brand__text{display:flex;flex-direction:column;line-height:1.1}
  .brand__name{font-weight:400;color:var(--grey-dark);white-space:nowrap}
  .brand__tagline{font-weight:400;color:var(--ink);white-space:nowrap;letter-spacing:.02em}

  /* letterhead */
  .letterhead{left:60px;top:120px;width:400px;height:560px}
  .letterhead .brand{left:20px;top:30px}
  .letterhead .brand__mark{width:42px;height:42px}
  .letterhead .brand__name{font-size:12px}
  .letterhead .brand__tagline{font-size:7px}
  .letterhead__web{left:200px;right:0;top:20px;height:16px;justify-content:flex-end;padding-right:16px;font-size:7.5px;font-weight:400;text-transform:none}
  .letterhead__rule{left:196px;right:0;top:42px;height:14px}
  .letterhead__body{position:absolute;left:36px;right:36px;top:120px;font-size:7.6px;line-height:1.55;color:var(--ink)}
  .letterhead__body p{margin-bottom:10px}
  .letterhead__footer{left:0;right:0;bottom:22px;height:38px;flex-direction:column;align-items:flex-start;justify-content:center;padding-left:36px;font-size:7.5px;gap:3px}
  .letterhead__footer span{font-weight:400}

  /* envelope */
  .envelope{left:500px;top:120px;width:640px;height:278px}
  .envelope .brand{left:22px;top:36px}
  .envelope .brand__mark{width:48px;height:48px}
  .envelope .brand__name{font-size:14px}
  .envelope .brand__tagline{font-size:8px}
  .envelope__return{left:222px;right:84px;top:48px;height:22px;padding-left:10px;font-size:7.5px;letter-spacing:0}
  .envelope__return .divider{margin:0 5px;font-weight:400}
  .envelope__return .phone{font-weight:400}
  .envelope__stamp{position:absolute;right:18px;top:18px;width:54px;height:68px;border:1px solid var(--grey-light)}
  .envelope__mid{left:300px;right:0;top:150px;height:22px}
  .envelope__foot{left:0;right:0;bottom:22px;height:24px}

  /* business cards */
  .card{width:300px;height:171px;top:460px}
  .card--front{left:500px}
  .card--front .brand{left:12px;top:18px;gap:5px}
  .card--front .brand__mark{width:30px;height:30px}
  .card--front .brand__name{font-size:9.5px}
  .card--front .brand__tagline{font-size:5.8px}
  .card__title{left:156px;right:0;top:26px;height:16px;padding-left:7px;font-size:6px;letter-spacing:0}
  .card__title .role{font-weight:400;margin-left:5px;padding-left:5px;border-left:1px solid var(--white)}
  .card__address,.card__contact{position:absolute;bottom:18px;font-size:6.8px;line-height:1.6;color:var(--grey-dark)}
  .card__address{left:16px}
  .card__contact{left:160px}
  .card__contact b{color:var(--ink);font-weight:700;margin-right:3px}
  .card--back{left:840px;background:var(--grey-dark);display:flex;align-items:center;justify-content:center}
  .card--back .brand{position:static;gap:10px}
  .card--back .brand__mark{width:60px;height:60px;border-color:var(--white)}
  .card--back .brand__name{color:var(--white);font-size:16px}
  .card--back .brand__tagline{color:var(--grey-pale);font-size:9px}
</style>
</head>
<body>

<section class="sheet letterhead" aria-label="Letterhead">
  <div class="brand">
    <span class="brand__mark"></span>
    <span class="brand__text"><span class="brand__name">Welbourne Dental</span><span class="brand__tagline">General &amp; Cosmetic Dentistry</span></span>
  </div>
  <div class="band letterhead__web">www.welbournedental.com</div>
  <div class="band band--dark letterhead__rule"></div>
  <div class="letterhead__body">
    <p>Lorem Ipsum is simply dummy text of the printing and typesetting industry. Lorem Ipsum has been the industry's standard dummy text ever since the 1500s, when an unknown printer took a galley of type and scrambled it to make a type specimen book. It has survived not only five centuries, but also the leap into electronic typesetting, remaining essentially unchanged. It was popularised in the 1960s with the release of Typeframe sheets containing Lorem Ipsum passages, and more recently with desktop publishing software like Quillset Composer including versions of Lorem Ipsum.</p>
    <p>It is a long established fact that a reader will be distracted by the readable content of a page when looking at its layout. The point of using Lorem Ipsum is that it has a more-or-less normal distribution of letters, as opposed to using 'Content here, content here', making it look like readable English. Many desktop publishing packages and web page editors now use Lorem Ipsum as their default model text, and many web sites still in their infancy have evolved over the years, sometimes by accident, sometimes on purpose.</p>
    <p>Contrary to popular belief, Lorem Ipsum is not simply random text. It has roots in a piece of classical Latin literature, making it over 2000 years old. Edwin Castellane, a Latin professor, looked up one of the more obscure Latin words, and going through the cites of the word in classical literature, discovered the undoubtable source. Lorem Ipsum comes from sections 1.10.32 and 1.10.33 of "de Finibus Bonorum et Malorum" (The Extremes of Good and Evil) by Cicero, written in 45 BC. This book is a treatise on the theory of ethics, very popular during the Renaissance. The first line of Lorem Ipsum comes from a line in section 1.10.32.</p>
  </div>
  <div class="band band--dark letterhead__footer">
    <span>|P| (718)555-0193</span>
    <div>4352 63rd Ave, Lower Level, Brooklyn, NY 11290</div>
  </div>
</section>

<section class="sheet envelope" aria-label="Envelope">
  <div class="brand">
    <span class="brand__mark"></span>
    <span class="brand__text"><span class="brand__name">Welbourne Dental</span><span class="brand__tagline">General &amp; Cosmetic Dentistry</span></span>
  </div>
  <div class="band band--dark envelope__return">4352 63rd Ave, Lower Level, Brooklyn, NY 11290<span class="divider">|</span><span class="phone">|P| (718)555-0193</span></div>
  <div class="envelope__stamp"></div>
  <div class="band envelope__mid"></div>
  <div class="band envelope__foot"></div>
</section>

<section class="sheet card card--front" aria-label="Business card, front">
  <div class="brand">
    <span class="brand__mark"></span>
    <span class="brand__text"><span class="brand__name">Welbourne Dental</span><span class="brand__tagline">General &amp; Cosmetic Dentistry</span></span>
  </div>
  <div class="band band--dark card__title">Marisol Dubrovka<span class="role">Office Manager</span></div>
  <div class="card__address">4352 63rd Ave<br>Lower Level<br>Brooklyn, NY 11290</div>
  <div class="card__contact"><b>|P|</b>(718)555-0193<br><b>|F|</b>(718)555-0194<br><b>|E|</b>info@welbournedental.com</div>
</section>

<section class="sheet card card--back" aria-label="Business card, back">
  <div class="brand">
    <span class="brand__mark"></span>
    <span class="brand__text"><span class="brand__name">Welbourne Dental</span><span class="brand__tagline">General &amp; Cosmetic Dentistry</span></span>
  </div>
</section>

</body>
</html>
```